Employment Agency Website Design

We are working with an employment agency in California.

Some sites to use for content/competitors and inspiration:

https://www.dovelanejobs.example/us/en
https://www.perimowork.example
https://www.tamberlinehire.example
https://www.vintrastaff.example/en
https://www.olmirajobs.example
https://www.quarnstaffing.example

Thank you for taking the time to consider designing a website for us. We are web developers based in Stockton, CA, USA. Most of our projects go through the same process. Understanding this process may help you win a project with us. We custom-code all of our websites in-house. We don’t have any requirements as to what tools you use for your design, but we prefer Figma files. For any design that we label as four-stars, we send it to the client for review. The client picks the final design they want us to use. Once we complete this process, we will continue to show additional clients all the four-star sites and purchase them later. Your designs will have multiple chances to sell. For better chances of success, we ask that you follow these guidelines.

IMAGES:
If you use any images or icons in the design, we ask that you have a link to the asset so we can purchase the image/icon. Most of the designs we submit do not have the customer’s images on them unless they have some great images. Be creative; show us the feeling you are trying to portray with your image choices. Use any royalty-free site you choose. We subscribe to Velsor and mainly use their images, but we can purchase images outside of Velsor. PLEASE NOTE: we will not submit designs to clients with watermarks on the images.

FONTS:
We ask that you identify the fonts used in the design. This can be done in a message if you want. We typically use Google Fonts and Velsor Fonts.

CONTENT:
We're always open to different content and ideas. We often submit designs with stock images so the client can see our vision. We typically take pictures after the website launch to use their images with our vision. Lorem Ipsum is fine for paragraphs, but we ask that you write the headers in correct English. We want to be able to show the vision and identify the sections of the website.

INSPIRATION:
We typically add a couple of links in the brief of websites we like to help you get started in your design.

REVISIONS:
We do not often ask for revisions of the designs unless we see something in the design that may not appeal to the client. If there are slight changes that we want to make, we do that in the development process.

FEEDBACK:
We rarely give feedback on designs during the design process. We are working on many website projects and do not have the time to provide feedback. We usually respond if your request is well thought out and asks specific questions, but a note asking “feedback, please” usually goes unanswered.

```html
<!DOCTYPE html>
<html lang="en">
<head>
<meta charset="utf-8">
<title>Brightwell talent – Staffing &amp; Recruiting</title>
<link href="https://fonts.googleapis.com/css2?family=Lexend:wght@400;500;600&family=Poppins:wght@400;500;600&display=swap" rel="stylesheet">
<style>
:root{
  --red:#c3121f;
  --red-dark:#9e0e18;
  --ink:#141414;
  --text:#3a3a3a;
  --muted:#6d6d6d;
  --line:#e4e4e4;
  --soft:#f3f3f3;
  --white:#ffffff;
}
*{box-sizing:border-box;margin:0;padding:0}
html,body{width:1200px;height:4307px;overflow:hidden}
body{position:relative;font-family:"Poppins",sans-serif;color:var(--text);background:var(--white)}
.abs{position:absolute}
h1,h2,h3{font-family:"Lexend",sans-serif;font-weight:500;color:var(--ink)}
a{color:inherit}

/* header */
.topbar{left:0;top:0;width:1200px;height:33px}
.topbar-links{top:0;left:735px;height:33px;display:flex;align-items:center;font-size:11px;color:var(--white)}
.topbar-links span{display:flex;align-items:center;gap:6px}
.header{left:0;top:33px;width:1200px;height:67px;border-bottom:1px solid var(--line)}
.brand{left:110px;top:26px;display:flex;align-items:center;gap:10px}
.brand-mark{width:34px;height:34px;background:var(--red)}
.brand-name{font-family:"Lexend",sans-serif;font-size:29px;font-weight:500;color:var(--ink);line-height:1}
.brand-tag{left:160px;top:66px;font-size:11px;color:var(--muted)}
.nav{left:461px;top:58px;display:flex;gap:28px;font-size:12px;color:var(--ink)}
.nav span::after{content:"";display:inline-block;margin-left:7px;border:4px solid transparent;border-top:5px solid var(--red);vertical-align:-1px}
.btn-dark{background:var(--ink);color:var(--white);font-size:12px;font-weight:500;display:flex;align-items:center;justify-content:center}
.contact-btn{left:964px;top:48px;width:126px;height:37px}

/* hero */
.hero-photo{left:0;top:100px;width:1200px;height:630px;background:linear-gradient(90deg,#1b1b1d 0%,#3a3533 45%,#6b5f58 75%,#4a403c 100%)}
.hero-title{left:112px;top:202px;font-size:43px;line-height:52px;color:var(--white);font-weight:500}
.hero-sub{left:112px;top:316px;width:560px;font-size:15px;line-height:25px;color:#eee}
.tab-red{left:112px;top:389px;width:109px;height:30px;background:var(--red);color:var(--white);font-size:11px;display:flex;align-items:center;justify-content:center}
.tab-white{left:221px;top:389px;width:112px;height:30px;background:var(--white);color:var(--ink);font-size:11px;display:flex;align-items:center;justify-content:center}
.search{left:112px;top:419px;width:413px;height:44px;background:var(--white);display:flex;align-items:center;font-size:10px;color:var(--muted)}
.search .field{flex:1;padding-left:20px;display:flex;align-items:center;gap:6px}
.search .field+.field{border-left:1px solid var(--line)}
.search-btn{left:525px;top:419px;width:92px;height:44px;background:var(--red);color:var(--white);font-size:12px;display:flex;align-items:center;justify-content:center}

/* about */
.about-title{left:612px;top:818px;font-size:30px;line-height:36px}
.divider{display:flex;align-items:center;gap:6px}
.divider i{display:block;width:26px;height:1px;background:#bbb}
.divider b{display:block;width:10px;height:10px;background:var(--red)}
.about-div{left:612px;top:897px}
.about-copy{left:612px;top:930px;width:470px;font-size:12.5px;line-height:21px;color:var(--text)}
.about-copy p+p{margin-top:14px}
.about-btn{left:612px;top:1088px;width:209px;height:37px}

/* talent */
.talent-bg{left:0;top:1287px;width:1200px;height:646px;background:var(--soft)}
.talent-title{left:210px;top:1350px;font-size:33px}
.talent-card{left:110px;top:1417px;width:980px;height:438px;background:var(--white);border-top:3px solid var(--red);box-shadow:0 10px 30px rgba(0,0,0,.06)}
.types{left:210px;top:1440px;font-size:13px;font-weight:500;color:var(--ink);letter-spacing:.3px}
.arrow-circ{width:22px;height:22px;border-radius:50%;border:1.5px solid var(--red);display:flex;align-items:center;justify-content:center}
.job-tabs{left:110px;top:1484px;width:980px;height:34px;border-bottom:1px solid var(--line);display:flex;padding-left:100px;gap:0;font-size:11px;color:var(--ink)}
.job-tabs span{margin-right:40px;padding-top:6px}
.job-tabs .active{border-bottom:3px solid var(--red);height:34px;font-weight:500}
.job-copy{left:210px;top:1560px;width:340px;font-size:11.5px;line-height:17px;color:var(--muted)}
.trend-h{left:210px;top:1625px;font-size:13px;font-weight:500;color:var(--ink)}
.trend{font-size:10.5px;color:var(--ink);text-decoration:underline;line-height:24px}
.learn-btn{left:210px;top:1743px;width:120px;height:37px;font-size:11px}
.job-photo{left:648px;top:1552px;width:342px;height:265px;background:linear-gradient(135deg,#6b6560,#3d3936 60%,#8f8a84)}

/* interested */
.cta-title{left:0;top:2008px;width:1200px;text-align:center;font-size:33px;color:var(--white)}
.cta-sub{left:290px;top:2058px;width:620px;text-align:center;font-size:15px;line-height:25px;color:#fbe9ea}
.cta-btn{left:540px;top:2134px;width:120px;height:35px;background:var(--ink);border:1px solid #fff;color:var(--white);font-size:11px;display:flex;align-items:center;justify-content:center}

/* how */
.sec-title{left:0;width:1200px;text-align:center;font-size:35px}
.center-div{left:0;width:1200px;justify-content:center}
.step{width:280px;text-align:center}
.step-label{font-size:12.5px;font-weight:500;color:var(--ink);margin-top:26px;line-height:15px}

/* reviews */
.reviews-bg{left:0;top:2682px;width:1200px;height:510px;background:var(--soft)}
.review{top:2837px;width:296px;height:271px;background:var(--white);padding:22px 22px;box-shadow:0 6px 20px rgba(0,0,0,.04)}
.quote{font-family:Georgia,serif;font-size:90px;line-height:70px;color:#e1e1e1;height:54px}
.review p{margin-top:22px;font-size:11.5px;line-height:20px;color:var(--text)}
.reviewer{display:flex;align-items:center;gap:10px;margin-top:20px}
.avatar{width:52px;height:52px;border-radius:50%;border:2px solid var(--red);background:linear-gradient(135deg,#d9c1ad,#8e705c)}
.reviewer h4{font-family:"Lexend",sans-serif;font-weight:400;font-size:13px;color:var(--ink)}
.stars{color:var(--red);font-size:12px;letter-spacing:1px}

/* insights */
.post{top:3339px;width:247px}
.post-photo{width:247px;height:266px}
.post-date{margin-top:30px;font-size:10px;color:var(--red)}
.post-title{margin-top:14px;font-size:11px;line-height:15px;font-weight:500;color:var(--ink)}
.post-copy{margin-top:10px;font-size:10.5px;line-height:16px;color:var(--text)}
.post-arrow{margin-top:14px}

/* footer */
.foot-brand{left:150px;top:4070px;width:230px;text-align:center}
.foot-mark{width:70px;height:70px;border-radius:50%;background:var(--red);margin:0 auto 16px}
.foot-name{font-family:"Lexend",sans-serif;font-size:24px;font-weight:400;color:var(--white)}
.foot-tag{font-size:10px;color:#bbb;margin-top:2px}
.socials{display:flex;gap:8px;justify-content:center;margin-top:12px}
.socials span{width:31px;height:31px;border-radius:50%;border:1.5px solid #fff;background:var(--red)}
.foot-h{font-size:13px;font-weight:500;color:var(--white);letter-spacing:.5px}
.foot-item{display:flex;align-items:center;gap:10px;font-size:11px;color:#ddd}
.foot-links{font-size:11px;line-height:21.5px;color:#ccc}
.vline{width:1px;background:#333}
.copyright{left:0;top:4268px;width:1200px;text-align:center;font-size:10.5px;color:#bbb}
</style>
</head>
<body>

<!-- Top utility bar -->
<svg class="abs topbar" width="1200" height="33" viewBox="0 0 1200 33">
  <polygon points="719,0 1200,0 1200,33 735,33" fill="var(--red)"/>
  <rect x="930" y="0" width="1" height="33" fill="#e7656d"/>
  <rect x="1035" y="0" width="1" height="33" fill="#e7656d"/>
  <circle cx="772" cy="15" r="6" fill="none" stroke="#fff" stroke-width="1.5"/>
  <line x1="776" y1="19" x2="781" y2="24" stroke="#fff" stroke-width="1.5"/>
  <circle cx="1064" cy="16" r="7" fill="none" stroke="#fff" stroke-width="1.3"/>
  <line x1="1057" y1="16" x2="1071" y2="16" stroke="#fff" stroke-width="1"/>
  <ellipse cx="1064" cy="16" rx="3" ry="7" fill="none" stroke="#fff" stroke-width="1"/>
  <polygon points="1080,13 1088,13 1084,18" fill="#fff"/>
</svg>
<div class="abs topbar-links">
  <span style="margin-left:92px">Client Login
    <svg width="11" height="11" viewBox="0 0 11 11"><circle cx="5.5" cy="3.5" r="2.5" fill="none" stroke="#fff"/><path d="M1 10.5c0-3 9-3 9 0" fill="none" stroke="#fff"/></svg></span>
  <span style="margin-left:52px">Client Login
    <svg width="11" height="11" viewBox="0 0 11 11"><circle cx="5.5" cy="3.5" r="2.8" fill="#fff"/><path d="M0.5 11c0-4 10-4 10 0z" fill="#fff"/></svg></span>
</div>

<!-- Header -->
<div class="abs header"></div>
<div class="abs brand"><span class="brand-mark"></span><span class="brand-name">Brightwell talent</span></div>
<div class="abs brand-tag">The future of work.</div>
<nav class="abs nav">
  <span>Find Jobs</span><span>Hire talent</span><span>Explore Consulting Solutions</span><span>Discover Insights</span>
</nav>
<div class="abs btn-dark contact-btn">Contact Us</div>

<!-- Hero -->
<div class="abs hero-photo" role="img" aria-label="Photo of a team of business professionals talking in an office"></div>
<div class="abs" style="left:0;top:100px;width:760px;height:630px;background:linear-gradient(90deg,rgba(0,0,0,.55),rgba(0,0,0,0))"></div>
<h1 class="abs hero-title">Anything’s Possible<br>When You Have The Talent</h1>
<p class="abs hero-sub">Find skilled candidates, in-demand jobs and the solutions you need to help you do your best work yet.</p>
<div class="abs tab-red">Jobs Seekers</div>
<div class="abs tab-white">Employers</div>
<div class="abs search">
  <div class="field"><svg width="10" height="10" viewBox="0 0 10 10"><circle cx="4" cy="4" r="3" fill="none" stroke="#999"/><line x1="6.3" y1="6.3" x2="9" y2="9" stroke="#999"/></svg>Job title our keyword</div>
  <div class="field" style="padding-left:60px"><svg width="9" height="11" viewBox="0 0 9 11"><path d="M4.5 10.5S1 6.5 1 4.3a3.5 3.5 0 0 1 7 0c0 2.2-3.5 6.2-3.5 6.2z" fill="none" stroke="#999"/></svg>City, state or zip</div>
</div>
<div class="abs search-btn">Find Jobs</div>
<svg class="abs" style="left:0;top:540px" width="1200" height="192" viewBox="0 540 1200 192">
  <polygon points="0,600 600,727 1200,600 1200,732 0,732" fill="#fff"/>
  <polygon points="0,566 368,642 368,678 0,600" fill="var(--red)"/>
  <polygon points="1200,566 832,642 832,678 1200,600" fill="var(--red)"/>
</svg>

<!-- About -->
<svg class="abs" style="left:118px;top:762px" width="410" height="428" viewBox="0 0 410 428" role="img" aria-label="Photo of a smiling businesswoman working on a laptop">
  <defs><linearGradient id="aboutPhoto" x1="0" y1="0" x2="1" y2="1"><stop offset="0" stop-color="#d8d4cf"/><stop offset=".55" stop-color="#8a7563"/><stop offset="1" stop-color="#4a3a30"/></linearGradient></defs>
  <polygon points="140,4 6,82 6,238 140,316" fill="#8c8c8c"/>
  <polygon points="205,2 398,113 398,335 205,426 12,335 12,113" fill="var(--red)"/>
  <polygon points="200,6 388,114 388,330 200,420 12,330 12,114" fill="url(#aboutPhoto)"/>
</svg>
<h2 class="abs about-title">Bringing expertise together<br>with real partnership.</h2>
<div class="abs divider about-div"><b></b><i></i></div>
<div class="abs about-copy">
  <p>We believe the impact of the right job on your life is limitless. And for employers, the effect of the right talent on your business, at the right time, is just as big.</p>
  <p>That’s how we excel: by connecting people with great work that improves their lives, while also driving the success of the companies they choose. We bring it all together like no one else can.</p>
</div>
<div class="abs btn-dark about-btn">Working with Brightwell talent</div>

<!-- Specialized talent -->
<div class="abs talent-bg"></div>
<h2 class="abs talent-title">Add specialized talent across your organization</h2>
<div class="abs talent-card"></div>
<div class="abs types">TYPES OF JOB</div>
<div class="abs arrow-circ" style="left:927px;top:1438px;border-color:#bbb"><svg width="10" height="10" viewBox="0 0 10 10"><path d="M9 5H1M4.5 1.5 1 5l3.5 3.5" fill="none" stroke="#bbb" stroke-width="1.3"/></svg></div>
<div class="abs arrow-circ" style="left:967px;top:1438px"><svg width="10" height="10" viewBox="0 0 10 10"><path d="M1 5h8M5.5 1.5 9 5 5.5 8.5" fill="none" stroke="var(--red)" stroke-width="1.3"/></svg></div>
<div class="abs job-tabs">
  <span class="active">Finance &amp; Accounting</span><span>Technology</span><span>Administrative &amp; Customer Support</span><span>Marketing &amp; Creative</span><span>Legal</span><span>Hospitality</span>
</div>
<p class="abs job-copy">From accountants to CFOs, we’ll bring you top candidates with in-demand skills and experience and help manage the hiring process for you.</p>
<div class="abs trend-h">Trending job titles</div>
<div class="abs trend" style="left:210px;top:1652px">Controller<br>Senior accountant<br>Senior financial analyst</div>
<div class="abs trend" style="left:350px;top:1652px">Internal auditor<br>Accounts payable/receivable specialist<br>Bookkeeper</div>
<div class="abs btn-dark learn-btn">LEARN MORE</div>
<svg class="abs" style="left:622px;top:1552px" width="40" height="265" viewBox="0 0 40 265">
  <polygon points="26,0 40,0 40,265 26,265 14,160 26,100" fill="var(--red)"/>
  <polygon points="6,100 18,88 18,176 6,164" fill="var(--ink)"/>
</svg>
<div class="abs job-photo" role="img" aria-label="Photo of a businessman in a suit standing at a laptop"></div>

<!-- Interested CTA -->
<svg class="abs" style="left:0;top:1933px" width="1200" height="345" viewBox="0 1933 1200 345" role="img" aria-label="Red tinted photo of professionals working together">
  <defs><linearGradient id="ctaBg" x1="0" y1="0" x2="1" y2="0"><stop offset="0" stop-color="#c3121f"/><stop offset=".5" stop-color="#b4101c"/><stop offset="1" stop-color="#c71a26"/></linearGradient></defs>
  <polygon points="0,1933 1200,1933 1200,2155 600,2276 0,2155" fill="url(#ctaBg)"/>
</svg>
<h2 class="abs cta-title">Interested in working for Brightwell talent?</h2>
<p class="abs cta-sub">Find skilled candidates, in-demand jobs and the solutions you need to help you do your best work yet.</p>
<div class="abs cta-btn">Find Jobs</div>

<!-- How it works -->
<h2 class="abs sec-title" style="top:2345px">How it works</h2>
<div class="abs divider center-div" style="top:2398px"><i></i><b></b><i></i></div>

<div class="abs step" style="left:122px;top:2428px">
  <svg width="104" height="120" viewBox="0 0 104 120"><polygon points="52,3 100,31 100,89 52,117 4,89 4,31" fill="#fff" stroke="var(--red)" stroke-width="4"/>
  <rect x="34" y="42" width="36" height="24" fill="none" stroke="var(--ink)" stroke-width="1.8"/><rect x="40" y="52" width="4" height="10" fill="var(--red)"/><rect x="48" y="48" width="4" height="14" fill="var(--red)"/><rect x="56" y="46" width="4" height="16" fill="var(--red)"/>
  <circle cx="40" cy="74" r="3" fill="none" stroke="var(--ink)" stroke-width="1.6"/><circle cx="52" cy="74" r="3" fill="none" stroke="var(--ink)" stroke-width="1.6"/><circle cx="64" cy="74" r="3" fill="none" stroke="var(--ink)" stroke-width="1.6"/>
  <path d="M35 84c0-4 10-4 10 0M47 84c0-4 10-4 10 0M59 84c0-4 10-4 10 0" fill="none" stroke="var(--ink)" stroke-width="1.6"/></svg>
  <div class="step-label">1. Describe your need</div>
</div>
<div class="abs step" style="left:458px;top:2428px">
  <svg width="104" height="120" viewBox="0 0 104 120"><polygon points="52,3 100,31 100,89 52,117 4,89 4,31" fill="#fff" stroke="var(--red)" stroke-width="4"/>
  <rect x="46" y="38" width="12" height="12" fill="var(--red)"/><path d="M49 44l2 2 4-4" fill="none" stroke="#fff" stroke-width="1.5"/>
  <circle cx="52" cy="62" r="4" fill="none" stroke="var(--ink)" stroke-width="1.7"/><circle cx="38" cy="66" r="3.5" fill="none" stroke="var(--ink)" stroke-width="1.7"/><circle cx="66" cy="66" r="3.5" fill="none" stroke="var(--ink)" stroke-width="1.7"/>
  <path d="M44 78c0-6 16-6 16 0M31 80c0-5 13-5 13 0M60 80c0-5 13-5 13 0" fill="none" stroke="var(--ink)" stroke-width="1.7"/></svg>
  <div class="step-label">2. View matching candidates</div>
</div>
<div class="abs step" style="left:796px;top:2428px">
  <svg width="104" height="120" viewBox="0 0 104 120"><polygon points="52,3 100,31 100,89 52,117 4,89 4,31" fill="#fff" stroke="var(--red)" stroke-width="4"/>
  <circle cx="40" cy="46" r="4" fill="none" stroke="var(--ink)" stroke-width="1.7"/><path d="M33 58c0-6 14-6 14 0" fill="none" stroke="var(--ink)" stroke-width="1.7"/>
  <circle cx="64" cy="64" r="4" fill="none" stroke="var(--ink)" stroke-width="1.7"/><path d="M57 76c0-6 14-6 14 0" fill="none" stroke="var(--ink)" stroke-width="1.7"/>
  <path d="M52 44h12v8M48 70H36v-6" fill="none" stroke="var(--ink)" stroke-width="1.5"/><circle cx="52" cy="58" r="4" fill="var(--red)"/></svg>
  <div class="step-label">3. Connect with a recruiter to<br>consult and hire</div>
</div>

<!-- Reviews -->
<div class="abs reviews-bg"></div>
<h2 class="abs sec-title" style="top:2746px">Custom Reviews</h2>
<div class="abs divider center-div" style="top:2799px"><i></i><b></b><i></i></div>

<div class="abs review" style="left:110px">
  <div class="quote">“</div>
  <p>"Lorem ipsum dolor sit amet, cnsectetuar adipiscing elit. Mauris sagittis faucibusas mauris eget tincidunt. Proin fermentum it nisl eros, vel fermentum libero molestieas quis. Proin tincidunt sit amits"</p>
  <div class="reviewer"><div class="avatar" role="img" aria-label="Portrait of Marisa Kell"></div><div><h4>Marisa Kell</h4><div class="stars">★★★★★</div></div></div>
</div>
<div class="abs review" style="left:451px">
  <div class="quote">“</div>
  <p>"Lorem ipsum dolor sit amet, cnsectetuar adipiscing elit. Mauris sagittis faucibusas mauris eget tincidunt. Proin fermentum it nisl eros, vel fermentum libero molestieas quis. Proin tincidunt sit amits"</p>
  <div class="reviewer"><div class="avatar" role="img" aria-label="Portrait of Darren Holt" style="background:linear-gradient(135deg,#b99a83,#5a4438)"></div><div><h4>Darren Holt</h4><div class="stars">★★★★★</div></div></div>
</div>
<div class="abs review" style="left:792px">
  <div class="quote">“</div>
  <p>"Lorem ipsum dolor sit amet, cnsectetuar adipiscing elit. Mauris sagittis faucibusas mauris eget tincidunt. Proin fermentum it nisl eros, vel fermentum libero molestieas quis. Proin tincidunt sit amits"</p>
  <div class="reviewer"><div class="avatar" role="img" aria-label="Portrait of Neil Corbin" style="background:linear-gradient(135deg,#d3b7a8,#7a3e3c)"></div><div><h4>Neil Corbin</h4><div class="stars">★★★★★</div></div></div>
</div>

<!-- Insights -->
<h2 class="abs sec-title" style="top:3248px">Fluent in your fields and industries.</h2>
<div class="abs divider center-div" style="top:3300px"><i></i><b></b><i></i></div>

<article class="abs post" style="left:210px">
  <div class="post-photo" role="img" aria-label="Photo of two colleagues reviewing documents in an office" style="background:linear-gradient(135deg,#d6dce2,#8c97a3 55%,#b1323a)"></div>
  <div class="post-date">Jan 12, 2023</div>
  <div class="post-title">Are you finding it hard to stay healthy this winter season?</div>
  <p class="post-copy">Here are 16 tof resumes and couldn’t find a perfect fit? We know, looking for a new job can often be exhausting.ips to keep you healthy and boost your immunity...</p>
  <svg class="post-arrow" width="22" height="22" viewBox="0 0 22 22"><circle cx="11" cy="11" r="10" fill="none" stroke="var(--red)" stroke-width="1.5"/><path d="M6 11h10M12 7l4 4-4 4" fill="none" stroke="var(--red)" stroke-width="1.5"/></svg>
</article>
<article class="abs post" style="left:476px">
  <div class="post-photo" role="img" aria-label="Photo of a businesswoman taking notes at a desk" style="background:linear-gradient(135deg,#e4e2de,#7a7570 55%,#2a2a2a)"></div>
  <div class="post-date">Jan 12, 2023</div>
  <div class="post-title">Are you finding it hard to stay healthy this winter season?</div>
  <p class="post-copy">Here are 16 tof resumes and couldn’t find a perfect fit? We know, looking for a new job can often be exhausting.ips to keep you healthy and boost your immunity...</p>
  <svg class="post-arrow" width="22" height="22" viewBox="0 0 22 22"><circle cx="11" cy="11" r="10" fill="none" stroke="var(--red)" stroke-width="1.5"/><path d="M6 11h10M12 7l4 4-4 4" fill="none" stroke="var(--red)" stroke-width="1.5"/></svg>
</article>
<article class="abs post" style="left:742px">
  <div class="post-photo" role="img" aria-label="Photo of a business meeting around a conference table" style="background:linear-gradient(135deg,#c9d4dc,#5f6b78 55%,#9c6a5a)"></div>
  <div class="post-date">Jan 12, 2023</div>
  <div class="post-title">Are you finding it hard to stay healthy this winter season?</div>
  <p class="post-copy">Here are 16 tof resumes and couldn’t find a perfect fit? We know, looking for a new job can often be exhausting.ips to keep you healthy and boost your immunity...</p>
  <svg class="post-arrow" width="22" height="22" viewBox="0 0 22 22"><circle cx="11" cy="11" r="10" fill="none" stroke="var(--red)" stroke-width="1.5"/><path d="M6 11h10M12 7l4 4-4 4" fill="none" stroke="var(--red)" stroke-width="1.5"/></svg>
</article>

<!-- Footer -->
<svg class="abs" style="left:0;top:3870px" width="1200" height="437" viewBox="0 3870 1200 437">
  <polygon points="0,4003 501,3925 698,3925 1200,4003 1200,4307 0,4307" fill="var(--ink)"/>
  <polygon points="501,3877 698,3877 698,3935 600,3914 501,3935" fill="var(--red)"/>
  <polygon points="368,3948 501,3925 501,3935 368,3958" fill="var(--ink)"/>
</svg>
<div class="abs foot-brand">
  <div class="foot-mark"></div>
  <div class="foot-name">Brightwell talent</div>
  <div class="foot-tag">The future of work</div>
  <div class="socials"><span></span><span></span><span></span></div>
</div>
<div class="abs vline" style="left:428px;top:4050px;height:160px"></div>
<div class="abs vline" style="left:806px;top:4050px;height:160px"></div>
<div class="abs foot-h" style="left:510px;top:4048px">CONTACT US</div>
<div class="abs foot-item" style="left:510px;top:4096px">
  <svg width="12" height="14" viewBox="0 0 12 14"><path d="M6 13S1.5 8 1.5 5a4.5 4.5 0 0 1 9 0c0 3-4.5 8-4.5 8z" fill="none" stroke="#ddd"/><circle cx="6" cy="5" r="1.6" fill="none" stroke="#ddd"/></svg>480 Harbor Mill Rd, Suite 210</div>
<div class="abs foot-item" style="left:510px;top:4142px;font-weight:600;color:#fff">
  <svg width="13" height="13" viewBox="0 0 13 13"><path d="M3 1l2 3-1.3 1.3a7 7 0 0 0 4 4L9 8l3 2-1 2C6 12.5.5 7 1 2z" fill="none" stroke="#ddd"/></svg>+1 555-014-2290</div>
<div class="abs foot-item" style="left:510px;top:4188px;text-decoration:underline">
  <svg width="13" height="10" viewBox="0 0 13 10"><rect x=".5" y=".5" width="12" height="9" fill="none" stroke="var(--red)"/><path d="M.5.5l6 5 6-5" fill="none" stroke="var(--red)"/></svg>hello@brightwelltalent.example</div>
<div class="abs foot-h" style="left:889px;top:4048px">QUICK LINKS</div>
<div class="abs foot-links" style="left:892px;top:4092px">Find Jobs<br>Hire talent<br>Explore Consulting<br>Solutions<br>Discover Insights<br>Contact Us</div>
<div class="abs" style="left:110px;top:4240px;width:980px;height:1px;background:#2c2c2c"></div>
<div class="abs copyright">© 2024 Brightwell talent All Rights Reserved.</div>

</body>
</html>
```